Business card for Internet Marketing Consultant

Simple - need a nice business card design using the logo elements and colors. Keywords: Progressive, professional, stylish, minimalist. Please use the bc as part of the design.

Info for card:

Gareth Pennick
Internet Marketing Strategist
Phone: (520) 318-6047
Email: gareth@brightcanopy.com
Address: 2915 W. Larkmoor Ave., Ste. 118
Tucson, Arizona 85293

Website: www.brightcanopy.com

Industry/Entity Type

Business

Font styles to use
Sans Serif

```html
<!DOCTYPE html>
<html lang="en">
<head>
<meta charset="utf-8">
<title>brightcanopy business card</title>
<link rel="stylesheet" href="https://fonts.googleapis.com/css2?family=Open+Sans:ital,wght@0,400;0,600;0,700;1,400&display=swap">
<style>
  :root {
    --bg: #e9ebee;
    --brand-blue: #2f69b3;
    --brand-blue-dark: #275c9f;
    --brand-green: #79bf5f;
    --ink-grey: #6b6d70;
    --ink-dark: #3a3c3f;
    --paper: #ffffff;
  }
  * { box-sizing: border-box; margin: 0; padding: 0; }
  html, body { width: 1200px; height: 900px; overflow: hidden; }
  body {
    background: var(--bg);
    font-family: "Open Sans", Arial, sans-serif;
    position: relative;
  }
  .card {
    position: absolute;
    width: 560px;
    height: 320px;
    border-radius: 4px;
    box-shadow: 0 6px 18px rgba(0,0,0,0.12);
    overflow: hidden;
  }

  /* Front: blue side */
  .card-front {
    left: 90px;
    top: 100px;
    background: var(--brand-blue);
    color: var(--paper);
  }
  .front-circle {
    position: absolute;
    right: -40px;
    top: -70px;
    width: 260px;
    height: 260px;
    border-radius: 50%;
    background: rgba(255,255,255,0.09);
  }
  .front-identity {
    position: absolute;
    left: 40px;
    bottom: 38px;
  }
  .front-name {
    font-size: 40px;
    font-weight: 700;
    letter-spacing: -0.5px;
    line-height: 1;
  }
  .front-tagline {
    margin-top: 6px;
    font-size: 13px;
    letter-spacing: 4px;
    opacity: 0.85;
  }
  .front-web {
    margin-top: 8px;
    font-size: 17px;
    font-weight: 600;
    letter-spacing: 1.5px;
  }

  /* Back: white side */
  .card-back {
    left: 550px;
    top: 480px;
    background: var(--paper);
  }
  .brand-lockup {
    position: absolute;
    left: 0;
    right: 0;
    top: 40px;
    display: flex;
    flex-direction: column;
    align-items: center;
  }
  .brand-row {
    display: flex;
    align-items: center;
    gap: 12px;
  }
  .brand-dot {
    width: 34px;
    height: 34px;
    border-radius: 50%;
    background: var(--brand-green);
  }
  .brand-name {
    font-size: 38px;
    font-weight: 700;
    color: var(--brand-blue);
    letter-spacing: -0.5px;
    line-height: 1;
  }
  .brand-tagline {
    margin-top: 6px;
    font-size: 12.5px;
    letter-spacing: 4px;
    color: var(--ink-grey);
  }
  .details {
    position: absolute;
    left: 0;
    right: 0;
    top: 170px;
    display: flex;
    justify-content: center;
  }
  .person {
    text-align: right;
    padding-right: 18px;
    border-right: 2px solid var(--brand-green);
    padding-top: 4px;
  }
  .person-name {
    font-size: 22px;
    font-weight: 700;
    color: var(--brand-blue-dark);
    line-height: 1.1;
  }
  .person-title {
    font-size: 14px;
    color: var(--ink-grey);
    margin-top: 2px;
  }
  .person-address {
    font-size: 14px;
    color: var(--ink-grey);
    margin-top: 10px;
    line-height: 1.4;
    font-style: normal;
  }
  .contact-list {
    list-style: none;
    padding-left: 16px;
  }
  .contact-item {
    display: flex;
    align-items: center;
    gap: 9px;
    font-size: 14.5px;
    color: var(--ink-dark);
    line-height: 22px;
  }
  .contact-item.is-strong { font-weight: 600; }
  .contact-icon {
    width: 12px;
    height: 12px;
    fill: var(--brand-blue);
    flex: none;
  }
</style>
</head>
<body>

  <section class="card card-front" aria-label="Card front">
    <div class="front-circle"></div>
    <div class="front-identity">
      <div class="front-name">brightcanopy</div>
      <div class="front-tagline">INTERNET MARKETING STRATEGIES</div>
      <div class="front-web">www.brightcanopy.com</div>
    </div>
  </section>

  <section class="card card-back" aria-label="Card back">
    <div class="brand-lockup">
      <div class="brand-row">
        <span class="brand-dot"></span>
        <span class="brand-name">brightcanopy</span>
      </div>
      <div class="brand-tagline">INTERNET MARKETING STRATEGIES</div>
    </div>

    <div class="details">
      <div class="person">
        <div class="person-name">Gareth Pennick</div>
        <div class="person-title">Managing Member</div>
        <address class="person-address">2915 W. Larkmoor Ave., Ste. 118<br>Tucson, AZ 85293</address>
      </div>
      <ul class="contact-list">
        <li class="contact-item">
          <svg class="contact-icon" viewBox="0 0 12 12" aria-hidden="true"><path d="M2.4 0.8 L4.2 2.8 L3.2 4.2 C3.8 5.6 6.4 8.2 7.8 8.8 L9.2 7.8 L11.2 9.6 L9.8 11.2 C5.4 11 1 6.6 0.8 2.2 Z"/></svg>
          (520) 318-6047
        </li>
        <li class="contact-item">
          <svg class="contact-icon" viewBox="0 0 12 12" aria-hidden="true"><rect x="3" y="0.5" width="6" height="3.5"/><rect x="0.5" y="4.5" width="11" height="5" rx="1"/><rect x="3" y="9" width="6" height="2.5"/></svg>
          (520) 318-6048
        </li>
        <li class="contact-item">
          <svg class="contact-icon" viewBox="0 0 12 12" aria-hidden="true"><path d="M3 0 H9 A1 1 0 0 1 10 1 V11 A1 1 0 0 1 9 12 H3 A1 1 0 0 1 2 11 V1 A1 1 0 0 1 3 0 Z M3.2 1.5 V9.5 H8.8 V1.5 Z"/></svg>
          (520) 904-2215
        </li>
        <li class="contact-item is-strong">
          <svg class="contact-icon" viewBox="0 0 12 12" aria-hidden="true"><path d="M0.5 2.5 H11.5 V3 L6 6.8 L0.5 3 Z M0.5 4.2 L6 8 L11.5 4.2 V9.5 H0.5 Z"/></svg>
          gareth@brightcanopy.com
        </li>
        <li class="contact-item is-strong">
          <svg class="contact-icon" viewBox="0 0 12 12" aria-hidden="true"><path d="M6 0.5 A5.5 5.5 0 1 0 6 11.5 A5.5 5.5 0 1 0 6 0.5 Z M6 1.6 C6.9 2.6 7.3 4 7.4 5.4 H4.6 C4.7 4 5.1 2.6 6 1.6 Z M4.6 6.6 H7.4 C7.3 8 6.9 9.4 6 10.4 C5.1 9.4 4.7 8 4.6 6.6 Z M1.7 5.4 C1.9 3.7 3 2.3 4.5 1.8 C3.9 2.9 3.5 4.1 3.4 5.4 Z M1.7 6.6 H3.4 C3.5 7.9 3.9 9.1 4.5 10.2 C3 9.7 1.9 8.3 1.7 6.6 Z M8.6 5.4 C8.5 4.1 8.1 2.9 7.5 1.8 C9 2.3 10.1 3.7 10.3 5.4 Z M8.6 6.6 H10.3 C10.1 8.3 9 9.7 7.5 10.2 C8.1 9.1 8.5 7.9 8.6 6.6 Z"/></svg>
          www.brightcanopy.com
        </li>
      </ul>
    </div>
  </section>

</body>
</html>
```